Women's Clinic professional statement

Letterhead for an OBGYN practice that can be used as letterhead but also for patient info and memos, eventually maybe post on the web as email template. I guess that would be an HTML file. I envision a decorative banner head. I like the "Dr. Whitcombe" style and colors. I am not a realtor, but I like that layout, but no bars on the side, I need the space for text and I have no links. Small bottom banner. An ocean beach scene could work. See my older personal letterhed. I am on Guam. Guam is a tropical island

Target Market(s)

Current and future patients, colleagues, other clinics, hospitals, medical facilities

Industry/Entity Type

Health And Wellness

Font styles to use
Serif

Colors
0a90cc
f89831

Requirements
Must have
• I am open to suggestions
Nice to have
• Warm tone. Friendly but not sweet or saccharine. Authoritive, authentic, and upscale classic, but approachable. The Dr. Whitcombe hits that pretty well. Ethnically neutral. On color I am torn between light blue, like my caduceus letterhead and the warm yellow tones of Dr. Whitcombe.
Should not have
• No cutesy graphics, baby ducks and cats. Real photos of women difficult. No body shaming fitness caucasian women. The majority of my patients are pacific islanders (heavy set), Korean, and Chinese (petite skinny), only 10% caucasian. On the masculine-feminine scale: Must appeal to women, trustworthy to women, but I am male. Feminine would look phony.

```html
<!DOCTYPE html>
<html lang="en">
<head>
<meta charset="utf-8">
<title>Marcus R. Hallworth, MD, FACOG — Letterhead</title>
<link rel="stylesheet" href="https://fonts.googleapis.com/css2?family=Alegreya:wght@700&family=Roboto:wght@400&display=swap">
<style>
  :root {
    --page-bg: #eef6f1;
    --teal: #3bb3c4;
    --white: #ffffff;
    --ink: #444444;
    --ink-soft: #4a4a4a;
    --sea-deep: #1f3f73;
    --sea-mid: #3e6598;
    --foam: #e6edf2;
    --skin-warm: #d8b9a0;
    --cardigan: #cbb9a6;
    --hair: #3a2a22;
    --shirt: #f4f6f8;
  }
  * { box-sizing: border-box; margin: 0; padding: 0; }
  html, body { width: 1076px; height: 1200px; overflow: hidden; }
  body { background: var(--page-bg); position: relative; font-family: "Roboto", Arial, sans-serif; color: var(--ink); }

  .letterhead {
    position: absolute; left: 94px; top: 126px; width: 887px; height: 965px;
    background: var(--teal); border-radius: 16px; overflow: hidden;
  }
  .masthead { position: absolute; left: 34px; top: 18px; color: var(--white); }
  .doctor-name { font-family: "Alegreya", Georgia, serif; font-weight: 700; font-size: 39px; line-height: 1.2; letter-spacing: 0.3px; }
  .doctor-title { font-size: 18px; line-height: 1.3; margin-top: 0; }

  .contact-panel { position: absolute; left: 4px; top: 106px; width: 879px; height: 138px; background: var(--white); }
  .contact { position: absolute; left: 30px; top: 42px; font-size: 18px; line-height: 23px; color: var(--ink-soft); }

  .letter-body { position: absolute; left: 4px; top: 286px; width: 879px; height: 461px; background: var(--white); }
  .letter { position: absolute; left: 24px; top: 38px; width: 832px; font-size: 13px; line-height: 17.6px; text-align: justify; }
  .letter p { margin-bottom: 17.6px; }
  .letter .closing { margin-top: 34px; margin-bottom: 34px; }
  .letter .signature { text-align: left; }

  .ocean-banner {
    position: absolute; left: 4px; top: 779px; width: 879px; height: 182px;
    background: linear-gradient(180deg, var(--sea-deep) 0%, var(--sea-mid) 60%, var(--foam) 85%, #c9d4dc 100%);
    border-radius: 0 0 12px 12px;
  }

  .portrait-expectant {
    position: absolute; left: 744px; top: 32px; width: 232px; height: 338px;
    background: linear-gradient(160deg, var(--hair) 0%, var(--hair) 22%, var(--cardigan) 45%, var(--skin-warm) 100%);
    border-radius: 90px 40px 0 60px;
  }
  .portrait-doctor {
    position: absolute; left: 620px; top: 772px; width: 357px; height: 317px;
    background: linear-gradient(180deg, #8f8a86 0%, #c9a490 30%, var(--shirt) 62%, var(--shirt) 100%);
    border-radius: 140px 140px 12px 0;
  }
</style>
</head>
<body>
  <div class="letterhead">
    <header class="masthead">
      <h1 class="doctor-name">Marcus R. Hallworth, MD, FACOG</h1>
      <p class="doctor-title">Board Certified Obstetrician &amp; Gynecologist</p>
    </header>

    <section class="contact-panel">
      <address class="contact" style="font-style:normal">
        PO Box 482017, Tamuning, GU 96931<br>
        Tel: 671-555-0148 / drhallworthclinic@mail.com
      </address>
    </section>

    <main class="letter-body">
      <div class="letter">
        <p>Dear Recipient</p>
        <p>&nbsp;Lorem ipsum dolor sit amet, consectetur adipiscing elit. Cras vestibulum leo et vulputate sodales. Aenean a leo elementum libero bibendum hendrerit in eu libero. Aenean dignissim ipsum arcu, vitae vestibulum ante cursus eu. Integer blandit id tortor nec vulputate. Donec nec orci ipsum.</p>
        <p>Class aptent taciti sociosqu ad litora torquent per conubia nostra, per inceptos himenaeos. Etiam porta aliquam metus quis tempus. Sed et eleifend nibh. Curabitur commodo magna in ipsum fringilla, ut blandit dui tristique. Vivamus tempor ullamcorper interdum. Quisque purus orci, posuere ut venenatis ut, pretium a nunc. Vestibulum nec mauris iaculis, hendrerit velit nec, tristique mi. Lorem ipsum dolor sit amet, consectetur adipiscing elit. Cras vestibulum leo et vulputate sodales. Aenean a leo elementum libero bibendum hendrerit in eu libero. Aenean dignissim ipsum arcu, vitae vestibulum ante cursus eu. Integer blandit id tortor nec vulputate. Donec nec orci ipsum.</p>
        <p class="closing">Your Truly,</p>
        <p class="signature">The Name<br>The Dirctor<br>xyz address<br>1234569</p>
      </div>
    </main>

    <div class="ocean-banner" role="img" aria-label="Photo of a tropical ocean with waves breaking on the shore"></div>
  </div>

  <div class="portrait-expectant" role="img" aria-label="Photo of an expectant mother in a light cardigan, smiling down at her belly"></div>
  <div class="portrait-doctor" role="img" aria-label="Portrait photo of the doctor in a white polo shirt"></div>
</body>
</html>
```